Dentures for adults and seniors, using new products and technology to attract a younger audience

I am a Denturist, which means I make dentures (false teeth). I am promoting myself (Rosalind Thorpe Dentures) within 2 separate dental offices, both with different names. I need a flyer (I can provide the content) that looks inviting and correctly portrays my business (which does not have a sign) WITHIN the 2 other businesses and addresses/locations. To be clear, I want to use my logo and also the 2 logos of the offices, but mine would be more distinct. A double sided 4x6 inch cardstock is what I'm after.

Target Market(s)

40+

Industry/Entity Type

Dental

Font styles to use
Serif
Sans Serif

Requirements
Must have
• PLEASE READ!!!!!!!!!!!!!
• 2 LOCATIONS!!!!!!!!!!!!!!!!!!!!!
• Bright Arc Dental Oral Wellness Centre (owc)
• 1784 Birchmont East Blvd, 2916 Lower Quarry Road,
• LaSalle Windsor
• A description of all the services
• The main logo (Rosalind Thorpe Dentures) more noticeable
Nice to have
• Basically, I want to make the flyer in the file "Flyer4" much more interesting, and add a bit of information. Some can be removed as well from the back page so as not to go into so much detail. OK SO FAR NO ONE HAS DONE IT RIGHT. I NEED THE FLYER TO CLEARLY SAY 2 LOCATIONS, WITH THE ADDRESSES OF EACH AND LOGO OF EACH.
Should not have
• THORPE DENTURE SERVICES!!!!!!!!!!!!

```html
<!DOCTYPE html>
<html lang="en">
<head>
<meta charset="utf-8">
<title>Rosalind Thorpe Dentures – Flyer</title>
<link rel="stylesheet" href="https://fonts.googleapis.com/css2?family=Exo+2:wght@600;800&family=Oswald:wght@600&family=Lato:ital,wght@0,400;1,700&family=Cinzel:wght@400&display=swap">
<style>
  :root {
    --sky: #29b3ea;
    --royal: #1b3fb8;
    --navy: #0d1f5c;
    --brand: #1da1dc;
    --brand-grey: #4a4f5a;
    --teal-text: #1f86b5;
    --white: #ffffff;
  }
  * { margin: 0; padding: 0; box-sizing: border-box; }
  html, body { width: 1200px; height: 871px; overflow: hidden; background: var(--white); }
  .flyer { position: relative; width: 1200px; height: 871px; overflow: hidden; background: var(--white); }

  .clinic-photo {
    position: absolute; left: 425px; top: 90px; width: 775px; height: 520px;
    background:
      linear-gradient(90deg, #ffffff 0%, rgba(255,255,255,0) 22%),
      linear-gradient(160deg, #dfe6ea 0%, #c8d4da 35%, #6fa9b3 60%, #e8d1bf 80%, #cfd9e0 100%);
  }
  .shapes { position: absolute; inset: 0; }

  .portrait {
    position: absolute; left: 82px; top: 384px; width: 320px; height: 320px;
    border-radius: 50%;
    background: radial-gradient(circle at 50% 45%, #c99a86 0%, #8a5f52 40%, #2a1d1a 75%);
  }

  .brand { position: absolute; left: 44px; top: 66px; }
  .brand-name {
    font-family: "Exo 2", sans-serif; font-weight: 600; font-size: 42px;
    line-height: 1; letter-spacing: 1px; color: var(--brand); white-space: nowrap;
  }
  .brand-sub {
    margin-top: 6px;
    font-family: "Cinzel", serif; font-size: 24px; letter-spacing: 9px;
    color: var(--brand-grey);
  }

  .call-line {
    position: absolute; left: 556px; top: 16px;
    font-family: "Oswald", sans-serif; font-weight: 600; font-size: 58px;
    color: var(--white); letter-spacing: 0.5px; white-space: nowrap;
  }

  .locations { position: absolute; left: 44px; top: 196px; width: 480px; }
  .locations-title {
    font-family: "Exo 2", sans-serif; font-weight: 800; font-size: 30px;
    line-height: 1.1; letter-spacing: 1px; color: var(--navy);
  }
  .office { display: flex; align-items: center; gap: 12px; margin-top: 10px; }
  .office-mark { flex: none; width: 34px; height: 34px; border-radius: 50%; background: var(--sky); }
  .office-name {
    font-family: "Exo 2", sans-serif; font-weight: 800; font-size: 21px;
    line-height: 1.15; color: var(--navy); white-space: nowrap;
  }
  .office-address {
    font-family: "Lato", sans-serif; font-weight: 400; font-size: 17px;
    line-height: 1.25; color: var(--brand-grey); white-space: nowrap;
  }

  .denturist-credit {
    position: absolute; left: 87px; top: 752px; width: 310px; text-align: center;
    font-family: "Lato", sans-serif; font-style: italic; font-weight: 700; font-size: 27px;
    line-height: 1.3; color: var(--white);
  }
  .specialty {
    position: absolute; right: 40px; top: 643px; text-align: right;
    font-family: "Cinzel", serif; font-weight: 400; font-size: 34px;
    line-height: 40px; letter-spacing: 2px; color: var(--teal-text);
  }
</style>
</head>
<body>
<main class="flyer">
  <div class="clinic-photo" role="img" aria-label="Photo of a denturist examining a smiling patient in a bright clinic"></div>

  <svg class="shapes" width="1200" height="871" viewBox="0 0 1200 871" aria-hidden="true">
    <path fill="var(--royal)" d="M440,0 L1200,0 L1200,168 C1050,108 900,110 760,160 C640,203 520,218 440,212 C500,150 512,70 440,0Z"/>
    <path fill="var(--sky)" d="M462,0 L1200,0 L1200,150 C1050,96 900,98 760,146 C640,188 530,202 462,200 C520,140 530,70 462,0Z"/>

    <path fill="none" stroke="var(--royal)" stroke-width="2" d="M0,540 C180,610 330,640 520,600 C700,565 850,545 1000,540"/>
    <path fill="none" stroke="var(--royal)" stroke-width="2" d="M0,560 C180,635 340,660 530,625 C700,595 850,575 980,568"/>

    <path fill="var(--royal)" d="M380,690 C650,600 950,538 1200,526 L1200,871 L380,871Z"/>
    <path fill="var(--sky)" d="M0,644 C150,690 320,705 470,665 C720,600 960,560 1200,552 L1200,871 L0,871Z"/>
    <path fill="var(--white)" d="M467,836 C600,722 800,640 1200,598 L1200,836Z"/>
    <path fill="var(--royal)" d="M420,836 L1200,836 L1200,871 L405,871Z"/>

    <circle cx="242" cy="544" r="186" fill="var(--royal)"/>
    <circle cx="242" cy="544" r="176" fill="var(--white)"/>
    <circle cx="242" cy="544" r="166" fill="var(--sky)"/>
  </svg>

  <div class="portrait" role="img" aria-label="Portrait photo of the denturist"></div>

  <div class="brand">
    <div class="brand-name">ROSALIND THORPE</div>
    <div class="brand-sub">DENTURES</div>
  </div>

  <div class="call-line">CALL US:555-204-1837</div>

  <section class="locations">
    <h1 class="locations-title">NOW AT 2 LOCATIONS</h1>
    <div class="office">
      <span class="office-mark"></span>
      <div>
        <p class="office-name">BRIGHT ARC DENTAL</p>
        <p class="office-address">1784 Birchmont East Blvd, LaSalle</p>
      </div>
    </div>
    <div class="office">
      <span class="office-mark"></span>
      <div>
        <p class="office-name">ORAL WELLNESS CENTRE (OWC)</p>
        <p class="office-address">2916 Lower Quarry Road, Windsor</p>
      </div>
    </div>
  </section>

  <p class="denturist-credit">ROSALIND THORPE, DD<br>DENTURIST</p>
  <p class="specialty">SPECIALIZING IN<br>NATURAL-LOOKING<br>DENTURES FOR KINDLY &amp;<br>PROFESSIONAL ADVICE, CALL</p>
</main>
</body>
</html>
```